Oven Cleaning flyer design

Hi there,
I need help designing a letterbox flyer. It needs to be DL size.
I have attached a rough design made with Chat GPT.
Would like back and front, have my business colors.
Please find attached mock up of what I would roughly like.
Also find attached logo.
Thank you

Target Market(s)

Home owners over 40

Industry/Entity Type

Cleaning

Requirements
Must have
• Logo, before after of oven, brand colors

```html
<!DOCTYPE html>
<html lang="en">
<head>
<meta charset="UTF-8">
<title>Gleamline Ovens – DL Flyer Front and Back</title>
<link href="https://fonts.googleapis.com/css2?family=Poppins:wght@400;500;600;700&display=swap" rel="stylesheet">
<style>
:root{
  --navy:#16214a;
  --teal:#45c1c9;
  --teal-dark:#3ab3bb;
  --red:#f2402e;
  --grey-bg:#6e6e6e;
  --panel-grey:#e8e8e8;
  --white:#ffffff;
  --ink:#1b1b1b;
}
*{margin:0;padding:0;box-sizing:border-box}
html,body{width:1200px;height:1182px;overflow:hidden}
body{background:var(--grey-bg);font-family:'Poppins',sans-serif;position:relative}
.flyer{position:absolute;top:43px;width:501px;height:1067px;background:var(--white);overflow:hidden;box-shadow:0 2px 6px rgba(0,0,0,.35)}
.flyer--front{left:86px}
.flyer--back{left:618px}
.abs{position:absolute}
.center{left:0;right:0;text-align:center}
.brand{display:flex;align-items:center;gap:12px}
.brand__dot{border-radius:50%;background:var(--teal)}
.brand__name{font-weight:700;color:var(--teal);letter-spacing:1px;line-height:1}
.headline{font-weight:700;font-size:48px;line-height:64px;color:var(--navy);letter-spacing:-1px}
.headline span{color:var(--teal)}
.lead{font-size:18.5px;line-height:23.5px;color:var(--ink)}
.photo{border-radius:14px}
.photo--before{background:linear-gradient(180deg,#5b5753 0%,#3a3836 45%,#8a5a2c 75%,#6e4a28 100%)}
.photo--after{background:linear-gradient(180deg,#eceeef 0%,#5b5f63 35%,#3b3e42 60%,#c9ccce 100%)}
.tag{color:var(--white);font-size:25px;text-align:center;line-height:36px;font-weight:500}
.tag--before{background:var(--red)}
.tag--after{background:var(--navy)}
.pill{background:var(--navy);color:var(--white);font-weight:700;border-radius:12px;text-align:center;border:2px solid var(--white)}
.phone{display:flex;align-items:center;justify-content:center;gap:6px;font-weight:700;letter-spacing:-1.5px}
.phone__icon{border-radius:50%;display:flex;align-items:center;justify-content:center}
.web{font-weight:500;letter-spacing:2.2px}
.feature{width:140px;text-align:center;font-size:17px;line-height:21px;letter-spacing:1.5px;color:var(--ink)}
.feature__icon{width:52px;height:52px;border-radius:50%;background:var(--navy);border:2px solid var(--white);box-shadow:0 0 0 2px var(--teal);margin:0 auto 14px;display:flex;align-items:center;justify-content:center}
.feature__icon--teal{background:var(--teal)}
</style>
</head>
<body>

<!-- FRONT -->
<section class="flyer flyer--front">
  <div class="abs center" style="top:66px;display:flex;justify-content:center">
    <div class="brand">
      <div class="brand__dot" style="width:54px;height:54px"></div>
      <div class="brand__name" style="font-size:38px">GLEAMLINE<br><span style="font-size:38px">OVENS</span></div>
    </div>
  </div>

  <h1 class="headline abs center" style="top:172px">Bring <span>Your Oven</span><br>Back to Life</h1>

  <p class="lead abs center" style="top:297px;padding:0 40px">Professional, non-caustic oven cleaning that removes built-up grease, smoke, and burnt grime - leaving your oven looking fresh again.</p>

  <svg class="abs" style="left:0;top:0" width="501" height="1067" viewBox="0 0 501 1067">
    <path d="M0 395 Q250 445 501 372 L501 1067 L0 1067 Z" fill="var(--teal)"/>
    <path d="M0 395 Q250 445 501 372" fill="none" stroke="var(--navy)" stroke-width="6"/>
    <path d="M0 933 Q250 800 501 957 L501 1067 L0 1067 Z" fill="var(--white)"/>
  </svg>

  <div class="photo photo--before abs" style="left:40px;top:468px;width:203px;height:322px" role="img" aria-label="Photo of a dirty oven interior with burnt grease on the door, before cleaning"></div>
  <div class="photo photo--after abs" style="left:254px;top:468px;width:208px;height:322px" role="img" aria-label="Photo of the same oven interior clean and shining, after cleaning"></div>
  <div class="tag tag--before abs" style="left:58px;top:774px;width:159px">Before</div>
  <div class="tag tag--after abs" style="left:274px;top:774px;width:164px">After</div>

  <div class="pill abs" style="left:122px;top:848px;width:229px;height:56px;font-size:44px;line-height:50px">Call Now</div>
  <p class="abs center" style="top:912px;font-size:27px;color:var(--ink)">Fast, Professional Service</p>
  <div class="phone abs center" style="top:950px;font-size:50px;color:var(--ink)">
    <span class="phone__icon" style="width:36px;height:36px;background:var(--teal)">
      <svg width="20" height="20" viewBox="0 0 24 24"><path d="M6.6 10.8a15 15 0 0 0 6.6 6.6l2.2-2.2a1 1 0 0 1 1-.25 11.4 11.4 0 0 0 3.6.57 1 1 0 0 1 1 1V20a1 1 0 0 1-1 1A17 17 0 0 1 3 4a1 1 0 0 1 1-1h3.5a1 1 0 0 1 1 1c0 1.25.2 2.45.57 3.57a1 1 0 0 1-.25 1z" fill="#fff"/></svg>
    </span>0400 182 539</div>
  <p class="web abs center" style="top:1000px;font-size:22px;color:var(--ink)">gleamlineovens.com.au</p>
</section>

<!-- BACK -->
<section class="flyer flyer--back">
  <div class="abs center" style="top:68px;display:flex;justify-content:center">
    <div class="brand">
      <div class="brand__dot" style="width:44px;height:44px"></div>
      <div class="brand__name" style="font-size:30px">GLEAMLINE<br>OVENS</div>
    </div>
  </div>

  <svg class="abs" style="left:0;top:0" width="501" height="1067" viewBox="0 0 501 1067">
    <path d="M0 113 Q250 200 501 121" fill="none" stroke="var(--navy)" stroke-width="6"/>
    <rect x="0" y="585" width="501" height="360" fill="var(--panel-grey)"/>
    <path d="M0 943 L0 900 Q250 690 501 900 L501 943 Z" fill="var(--teal)"/>
    <rect x="0" y="943" width="501" height="124" fill="var(--navy)"/>
  </svg>

  <div class="abs" style="left:43px;top:161px;width:148px;height:148px;border-radius:50%;background:linear-gradient(135deg,#8d8d8d,#3d3d3d);border:3px solid #fff" role="img" aria-label="Photo of a clean open oven with racks"></div>
  <div class="abs" style="left:304px;top:161px;width:148px;height:148px;border-radius:50%;background:linear-gradient(135deg,#a9a297,#3e3b36);border:3px solid #fff" role="img" aria-label="Photo of a clean barbecue grill"></div>
  <div class="abs" style="left:162px;top:141px;width:176px;height:176px;border-radius:50%;background:linear-gradient(160deg,#dcd6cc,#b49f7f 55%,#6fb6c4);border:3px solid #fff" role="img" aria-label="Photo of a gloved hand spraying and wiping a surface with a cloth"></div>

  <h2 class="abs center" style="top:322px;font-weight:500;font-size:35px;line-height:42px;color:var(--ink)">Why Choose</h2>
  <h2 class="abs center" style="top:362px;font-weight:700;font-size:33px;line-height:42px;color:var(--teal)">Gleamline Ovens?</h2>
  <p class="abs center" style="top:413px;padding:0 36px;font-size:15.8px;line-height:19.2px;color:var(--ink)">We're a local family business providing professional, non-caustic oven cleaning across Sunshine Coast. Using specialized-equipment and proven cleaning methods, we remove heavy grease, carbon build-up, smokeresidue, restoring your oven safely and effectively.</p>

  <svg class="abs" style="left:130px;top:545px" width="332" height="79" viewBox="0 0 332 79">
    <path d="M0 0 H332 L300 39 L332 79 H0 Z" fill="var(--red)" stroke="var(--navy)" stroke-width="1.5"/>
  </svg>
  <p class="abs" style="left:164px;top:548px;color:#fff;font-size:24px;line-height:30px">Mention this flyer for</p>
  <p class="abs" style="left:164px;top:576px;color:#fff;font-size:30px;line-height:38px;font-weight:700">your first clean</p>
  <div class="abs" style="left:39px;top:526px;width:110px;height:110px;border-radius:50%;background:var(--navy);border:4px solid #fff;text-align:center;color:#fff">
    <div style="font-weight:600;font-size:50px;line-height:56px;margin-top:10px"><span style="font-size:24px;vertical-align:top;color:var(--red)">$</span>10</div>
    <div style="font-weight:700;font-size:20px;letter-spacing:3px;color:var(--red);line-height:22px">OFF</div>
  </div>

  <div class="feature abs" style="left:12px;top:656px">
    <div class="feature__icon"><svg width="24" height="24" viewBox="0 0 24 24"><circle cx="12" cy="9" r="6" fill="none" stroke="#fff" stroke-width="2"/><path d="M9 9l2 2 4-4" fill="none" stroke="#fff" stroke-width="2"/></svg></div>
    Reliable<br>Service</div>
  <div class="feature abs" style="left:165px;top:652px">
    <div class="feature__icon feature__icon--teal"><svg width="24" height="24" viewBox="0 0 24 24"><circle cx="12" cy="12" r="8" fill="none" stroke="#fff" stroke-width="2"/><path d="M8 8l8 8M16 8l-8 8" stroke="#fff" stroke-width="2"/></svg></div>
    Non-Caustic<br>Cleaning</div>
  <div class="feature abs" style="left:328px;top:652px">
    <div class="feature__icon"><svg width="24" height="24" viewBox="0 0 24 24"><path d="M4 11h3v9H4zM9 20V11l4-7c1.5 0 2 1 2 2l-1 4h5a1.5 1.5 0 0 1 1.5 1.8l-1.5 7A1.5 1.5 0 0 1 17.5 20z" fill="#fff"/></svg></div>
    Satisfaction<br>Guaranteed</div>

  <div class="pill abs" style="left:136px;top:771px;width:230px;height:56px;font-size:44px;line-height:50px">Call Now</div>
  <div class="phone abs center" style="top:834px;font-size:50px;color:#fff">
    <span class="phone__icon" style="width:38px;height:38px;background:var(--navy)">
      <svg width="20" height="20" viewBox="0 0 24 24"><path d="M6.6 10.8a15 15 0 0 0 6.6 6.6l2.2-2.2a1 1 0 0 1 1-.25 11.4 11.4 0 0 0 3.6.57 1 1 0 0 1 1 1V20a1 1 0 0 1-1 1A17 17 0 0 1 3 4a1 1 0 0 1 1-1h3.5a1 1 0 0 1 1 1c0 1.25.2 2.45.57 3.57a1 1 0 0 1-.25 1z" fill="#fff"/></svg>
    </span>0400 182 539</div>
  <p class="web abs center" style="top:890px;font-size:21px;color:#fff;font-weight:600">gleamlineovens.com.au</p>

  <p class="abs center" style="top:952px;font-size:31px;line-height:39px;color:#fff">We also clean cooktops,<br>rangehoodsand BBQs</p>
</section>

</body>
</html>
```